Sumvera financial services stationery design

We need business stationery designed with letterheads, business cards, with compliments and envelope for a business that offers tax and accounting services
Updates

Designs look the same

Target Market(s)

Small to medium businesses, individuals, Self managed superfunds

Industry/Entity Type

Business

Font styles to use
Serif
Other font styles liked:
• Atlanta

Colors
32a6d6
3277b5

Requirements
Must have
• Logo incorporated with all my stationery
• professional
Should not have
• Lots of colours
• Busy

```html
<!DOCTYPE html>
<html lang="en">
<head>
<meta charset="utf-8">
<title>Sumvera Business Cards</title>
<link href="https://fonts.googleapis.com/css2?family=Cinzel:wght@600&family=Montserrat:wght@400;600&display=swap" rel="stylesheet">
<style>
  :root {
    --bg: #1c1c1c;
    --card: #111214;
    --white: #f2f2f2;
    --muted: #d4d4d4;
    --sky: #32a6d6;
    --ocean: #3277b5;
  }
  * { margin: 0; padding: 0; box-sizing: border-box; }
  html, body { width: 1200px; height: 738px; overflow: hidden; background: var(--bg); }
  .canvas {
    position: relative; width: 1200px; height: 738px;
    display: flex; align-items: center; justify-content: center; gap: 60px;
  }
  .card {
    position: relative; width: 510px; height: 292px; background: var(--card);
    border-radius: 3px; font-family: "Montserrat", sans-serif; color: var(--white);
    overflow: hidden;
  }
  .brand { display: flex; align-items: center; }
  .brand-square { background: var(--sky); flex: none; }
  .brand-name { font-family: "Cinzel", serif; font-weight: 600; color: var(--white); letter-spacing: 1px; white-space: nowrap; }

  .card-front .brand { position: absolute; left: 0; right: 0; top: 100px; justify-content: center; gap: 14px; }
  .card-front .brand-square { width: 58px; height: 58px; }
  .card-front .brand-name { font-size: 52px; line-height: 1; }
  .card-front .web { position: absolute; left: 0; right: 0; bottom: 44px; text-align: center; font-size: 13px; letter-spacing: .3px; }

  .card-back .brand { position: absolute; left: 38px; top: 128px; gap: 12px; }
  .card-back .brand-square { width: 36px; height: 36px; }
  .card-back .brand-name { font-size: 28px; line-height: 1; }
  .divider { position: absolute; left: 256px; top: 70px; width: 2px; height: 150px; background: var(--sky); }
  .details { position: absolute; left: 276px; top: 72px; right: 20px; }
  .person-name { font-size: 19px; font-weight: 600; color: var(--sky); letter-spacing: .5px; white-space: nowrap; }
  .person-role { font-size: 13px; margin-top: 2px; }
  .address { font-size: 12px; line-height: 1.35; margin-top: 20px; }
  .contacts { list-style: none; margin-top: 16px; font-size: 12px; line-height: 1.5; }
  .contacts li { display: flex; align-items: center; gap: 8px; white-space: nowrap; }
  .contacts svg { width: 9px; height: 9px; fill: var(--sky); flex: none; }
  .contacts .accent { color: var(--sky); }
</style>
</head>
<body>
<main class="canvas">
  <section class="card card-front">
    <div class="brand">
      <span class="brand-square"></span>
      <span class="brand-name">SUMVERA</span>
    </div>
    <p class="web">www.sumverafinance.com</p>
  </section>

  <section class="card card-back">
    <div class="brand">
      <span class="brand-square"></span>
      <span class="brand-name">SUMVERA</span>
    </div>
    <span class="divider"></span>
    <div class="details">
      <h1 class="person-name">DANIEL REYES</h1>
      <p class="person-role">Founder</p>
      <p class="address">480 Harbor Point Rd.<br>Coral Shore, FL 33100</p>
      <ul class="contacts">
        <li><svg viewBox="0 0 10 10"><path d="M2 0h2l1 3-1.5 1a5 5 0 0 0 2.5 2.5L7 5l3 1v2a2 2 0 0 1-2 2A8 8 0 0 1 0 2a2 2 0 0 1 2-2z"/></svg><span>555-201-4836</span></li>
        <li><svg viewBox="0 0 10 10"><path d="M0 2h10v6H0z M0 2l5 3.5L10 2" fill="none" stroke="#32a6d6" stroke-width="1.2"/></svg><span>info@sumverafinance.com</span></li>
        <li><svg viewBox="0 0 10 10"><circle cx="5" cy="5" r="4.3" fill="none" stroke="#32a6d6" stroke-width="1.2"/><path d="M1 5h8M5 1v8" stroke="#32a6d6" stroke-width="1"/></svg><span>www.<span class="accent">sumverafinance</span>.com</span></li>
      </ul>
    </div>
  </section>
</main>
</body>
</html>
```